Meridian Handsets business card design

I would like to see some designs for a business card for Meridian Handsets. I would like the business card to be double sided. It will need to have a similar colour / look and feel to our website www.meridianhandsets.com.au I have also attached our latest flyer. Final designs to be handed over in Photoshop format so that I can edit the business card when needed please.

Industry/Entity Type

Business

Contact Information for Business Card

Gavin Thornley
sales@meridianhandsets.com.au
Business Development Manager
ph: (08) 6197 5821
www.meridianhandsets.com.au

Font styles to use
Serif
Sans Serif

Requirements
Must have
• If you could please utilise our colour scheme as seen on our website and the attached flyer.
• I would also like the final design to be in a Photoshop format so that I can edit it when needed please.

```html
<!DOCTYPE html>
<html lang="en">
<head>
<meta charset="utf-8">
<title>Meridian Handsets – Business Card</title>
<link href="https://fonts.googleapis.com/css2?family=Open+Sans:wght@400;600&display=swap" rel="stylesheet">
<style>
  :root {
    --page-bg: #e9e7e4;
    --card-white: #ffffff;
    --ink-dark: #2f2f33;
    --brand-blue: #1b6fb8;
    --band-deep: #0d4fa3;
    --band-light: #1f7cc4;
    --accent-green: #5fc9a0;
    --text-white: #ffffff;
  }
  * { margin: 0; padding: 0; box-sizing: border-box; }
  html, body { width: 1200px; height: 1000px; overflow: hidden; }
  body {
    background: var(--page-bg);
    font-family: "Open Sans", Arial, sans-serif;
    position: relative;
  }
  .card {
    position: absolute;
    left: 265px;
    width: 666px;
    height: 397px;
    background: var(--card-white);
    overflow: hidden;
    box-shadow: 0 4px 12px rgba(0,0,0,0.18);
  }
  .card--front { top: 73px; }
  .card--back { top: 532px; }

  .wordmark {
    position: absolute;
    font-weight: 600;
    color: var(--ink-dark);
    letter-spacing: -0.5px;
    white-space: nowrap;
  }
  .card--front .wordmark { left: 32px; top: 42px; font-size: 40px; }

  .info-band {
    position: absolute;
    left: 0; top: 146px;
    width: 100%; height: 141px;
    background: radial-gradient(ellipse at 60% 10%, var(--band-light) 0%, var(--band-deep) 75%);
    color: var(--text-white);
  }
  .person-name { position: absolute; left: 33px; top: 10px; font-size: 19px; color: var(--accent-green); font-weight: 400; }
  .person-role { position: absolute; left: 33px; top: 35px; font-size: 15px; }
  .contact-list { position: absolute; left: 33px; top: 69px; list-style: none; font-size: 15px; line-height: 22px; }
  .contact-list li { display: flex; align-items: center; gap: 7px; }
  .contact-list svg { width: 14px; height: 14px; fill: var(--accent-green); }
  .office { position: absolute; left: 406px; top: 65px; font-size: 15px; line-height: 24px; }
  .office-name { color: var(--accent-green); }

  .product-strip { position: absolute; left: 0; top: 287px; width: 100%; height: 98px; }
  .product { position: absolute; background: linear-gradient(#4a4c52, #1e1f22); border-radius: 6px; }
  .product--desk { left: 85px; top: 12px; width: 86px; height: 72px; }
  .product--conference { left: 228px; top: 14px; width: 138px; height: 70px; background: linear-gradient(#bfc2c6, #3b3d41); }
  .product--headset { left: 405px; top: 8px; width: 58px; height: 80px; }
  .product--handset { left: 527px; top: 14px; width: 34px; height: 70px; }
  .accent-rule { position: absolute; left: 0; bottom: 0; width: 100%; height: 12px; background: var(--accent-green); }

  .backdrop-photo {
    position: absolute; inset: 0;
    background: radial-gradient(ellipse at 55% 35%, #e6e3e1 0%, #f1f0ef 45%, #fafafa 80%);
  }
  .card--back .wordmark { left: 0; width: 100%; text-align: center; top: 164px; font-size: 46px; }
  .tagline {
    position: absolute; left: 0; width: 100%; top: 230px;
    text-align: center; font-size: 22px; color: var(--ink-dark);
  }
</style>
</head>
<body>
  <section class="card card--front">
    <div class="wordmark">Meridian Handsets</div>
    <div class="info-band">
      <div class="person-name">Gavin Thornley</div>
      <div class="person-role">Business Development Manager</div>
      <ul class="contact-list">
        <li><svg viewBox="0 0 16 16"><path d="M2 6c0-2 2-3 6-3s6 1 6 3v1h-3V6H5v1H2z M4 8h8l1 5H3z"/></svg>(08) 6197 5821</li>
        <li><svg viewBox="0 0 16 16"><path d="M1 3h14v10H1z M1 3l7 6 7-6" stroke="#0d4fa3" stroke-width="1"/></svg>sales@meridianhandsets.com.au</li>
        <li><svg viewBox="0 0 16 16"><circle cx="8" cy="8" r="6.5"/><path d="M1.5 8h13M8 1.5v13" stroke="#0d4fa3" stroke-width="1"/></svg>www.meridianhandsets.com.au</li>
      </ul>
      <div class="office">
        <div class="office-name">Meridian Handsets</div>
        <div>Tenth Street, Lakemont</div>
        <div>Western Australia 6099 Australia</div>
      </div>
    </div>
    <div class="product-strip">
      <div class="product product--desk" role="img" aria-label="Desk IP phone product photo"></div>
      <div class="product product--conference" role="img" aria-label="Conference camera and speakerphone product photo"></div>
      <div class="product product--headset" role="img" aria-label="Wireless headset on base product photo"></div>
      <div class="product product--handset" role="img" aria-label="Cordless handset product photo"></div>
    </div>
    <div class="accent-rule"></div>
  </section>

  <section class="card card--back">
    <div class="backdrop-photo" role="img" aria-label="Faded photo of a businesswoman talking on a desk phone"></div>
    <div class="wordmark">Meridian Handsets</div>
    <div class="tagline">Phone systems for your business</div>
  </section>
</body>
</html>
```